Letterhead and Business card for Construction company

We need a letterhead and business card with our new company logo. We are based in NY. We develop and build properties.

The design should incorporate some unique feature from the logo (shape, font...). it should look like an extension from it.

Design should be clean and elegant, professional, not too busy.

The letterhead should include:
Logo (attached)
Address
Phone
Email

Please find the attached logo images and AI file.

Target Market(s)

Construction industry professionals

Industry/Entity Type

Construction, Development

Font styles to use
Sans Serif

Colors

Designer to choose colors to be used in the design.

Requirements
Must have
• Design should incorporate logo elements, additional assets are welcome. I'd like to see some other shapes / images invorporated too.

```html
<!DOCTYPE html>
<html lang="en">
<head>
<meta charset="utf-8">
<title>Halden Build — Letterhead</title>
<link href="https://fonts.googleapis.com/css2?family=Roboto:wght@400;700&display=swap" rel="stylesheet">
<style>
  :root {
    --backdrop: #dcdcdc;
    --paper: #f8f8f8;
    --ink: #231f20;
    --accent: #ee7a1e;
    --muted: #747474;
  }
  html, body {
    margin: 0;
    padding: 0;
    width: 1153px;
    height: 1200px;
    overflow: hidden;
    background: var(--backdrop);
    font-family: "Roboto", Arial, sans-serif;
  }
  .letterhead {
    position: absolute;
    left: 166px;
    top: 20px;
    width: 820px;
    height: 1160px;
    background: var(--paper);
    overflow: hidden;
  }
  .brand {
    position: absolute;
    left: 72px;
    top: 72px;
    display: flex;
    align-items: center;
    gap: 10px;
  }
  .brand-mark {
    width: 18px;
    height: 18px;
    background: var(--accent);
  }
  .brand-name {
    font-weight: 700;
    font-size: 30px;
    line-height: 1;
    color: var(--ink);
    letter-spacing: 0.5px;
  }
  .contact {
    position: absolute;
    left: 580px;
    top: 56px;
    font-size: 14px;
    line-height: 17px;
    color: var(--muted);
  }
  .contact-address { margin: 0 0 9px; }
  .contact-list { list-style: none; margin: 0; padding: 0; }
  .contact-list li { display: flex; align-items: center; gap: 5px; }
  .contact-list svg { width: 12px; height: 12px; flex: none; }
  .footer-band {
    position: absolute;
    left: 0;
    bottom: 0;
    width: 710px;
    height: 13px;
    background: var(--ink);
  }
  .footer-block {
    position: absolute;
    right: 0;
    bottom: 0;
    width: 13px;
    height: 13px;
    background: var(--accent);
  }
</style>
</head>
<body>
  <main class="letterhead">
    <header>
      <div class="brand">
        <span class="brand-mark"></span>
        <span class="brand-name">HALDEN BUILD</span>
      </div>
      <address class="contact" style="font-style:normal">
        <p class="contact-address">48 W Linden Ave Suite<br>7 Brookhaven NY 11719</p>
        <ul class="contact-list">
          <li>
            <svg viewBox="0 0 12 12" aria-hidden="true"><path fill="#ee7a1e" d="M1 4.5C1 2.5 3 1.5 6 1.5s5 1 5 3l-2.2.6-.4-1.3H3.6l-.4 1.3zM3 6l1-1.5h4L9 6v4.5H3z"/></svg>
            1-888-555-0142
          </li>
          <li>
            <svg viewBox="0 0 12 12" aria-hidden="true"><rect x="0.5" y="2.5" width="11" height="7.5" fill="#ee7a1e"/><path d="M1 3l5 4 5-4" fill="none" stroke="#f8f8f8" stroke-width="1"/></svg>
            info@haldenbuild.com
          </li>
          <li>
            <svg viewBox="0 0 12 12" aria-hidden="true"><circle cx="6" cy="6" r="5.5" fill="#ee7a1e"/><path d="M3 3.5c1 .3 1.5 1.2 1 2.2.8.4 1 1.3.6 2.3M8 2.5c-.5 1 .3 1.7 1.3 1.8M7.5 9.5c0-1 .8-1.6 1.8-1.5" fill="none" stroke="#f8f8f8" stroke-width="0.9"/></svg>
            www.haldenbuild.com
          </li>
        </ul>
      </address>
    </header>
    <div class="footer-band"></div>
    <div class="footer-block"></div>
  </main>
</body>
</html>
```